Owen Tasker Studios Business Card

Looking for a clear, modern, elegant, sharp business card that conveys a professional yet edgy image to my business as a wedding, portrait, and travel photographer. Would like something that looks vintage yet modern. Need a new business card to grow my business. We are growing the business for Wedding and Event Photography as well as fine art Photography. (Mostly Landscapes)
Updates

I’m looking through designs now but I have a new logo that i want using please.

New logo uploaded please redesign using that

PLEASE ALL DESIGNERS LOOK IN BRIEF FOR NEW LOGO

Target Market(s)

Brides, Grooms, Families with Kids, People looking for Fine Art Photography Artwork

Industry/Entity Type

Photographer

Contact Information for Business Card

Unsure

Font styles to use
Serif

Colors

Designer to choose colors to be used in the design.

Requirements
Must have
• My Website:
• http://taskerlens.examplefolio.net
• Phone:
• 323-481-5206
• Email:
• owentaskerlens@mailbox-example.net
Nice to have
• Would like a sort of shine on the printing finish.
• I like black I think it looks good on a business card.
• Can try working with my logo (png that I've attached)

```html
<!DOCTYPE html>
<html lang="en">
<head>
<meta charset="utf-8">
<title>Owen Tasker Studios – Business Card</title>
<link rel="stylesheet" href="https://fonts.googleapis.com/css2?family=Raleway:wght@300&family=EB+Garamond:wght@400&display=swap">
<style>
  :root {
    --card: #21222a;
    --ink: #ecebe6;
    --muted: #c9c8c3;
    --gold: #d7b44c;
    --bronze: #6b5635;
    --umber: #3a3430;
    --page: #ffffff;
  }
  html, body {
    margin: 0;
    padding: 0;
    width: 1200px;
    height: 900px;
    overflow: hidden;
    background: var(--page);
  }
  .canvas {
    position: relative;
    width: 1200px;
    height: 900px;
  }
  .card {
    position: absolute;
    top: 0;
    width: 502px;
    height: 900px;
    background: var(--card);
    overflow: hidden;
  }
  .card--front { left: 0; }
  .card--back { left: 698px; }
  .texture {
    position: absolute;
    inset: 0;
    width: 100%;
    height: 100%;
  }
  .brand {
    position: absolute;
    left: 0;
    right: 0;
    text-align: center;
    color: var(--ink);
    font-family: "Raleway", sans-serif;
    font-weight: 300;
  }
  .brand__mark {
    display: block;
    margin: 0 auto;
    border: 1.5px solid var(--ink);
    box-sizing: border-box;
  }
  .brand__name {
    display: block;
    white-space: nowrap;
    line-height: 1;
  }
  .brand__tag {
    display: block;
    line-height: 1;
  }
  .card--front .brand { top: 317px; }
  .card--front .brand__mark { width: 107px; height: 107px; }
  .card--front .brand__name { font-size: 50px; margin-top: 40px; letter-spacing: -0.5px; }
  .card--front .brand__tag { font-size: 19px; letter-spacing: 17px; margin-top: 18px; padding-left: 17px; }

  .card--back .brand { top: 173px; }
  .card--back .brand__mark { width: 59px; height: 59px; }
  .card--back .brand__name { font-size: 29px; margin-top: 22px; letter-spacing: -0.3px; }
  .card--back .brand__tag { font-size: 11px; letter-spacing: 9px; margin-top: 7px; padding-left: 9px; }

  .contact {
    position: absolute;
    margin: 0;
    padding: 0;
    list-style: none;
    color: var(--muted);
    font-family: "EB Garamond", serif;
  }
  .contact__item {
    position: absolute;
    display: flex;
    align-items: center;
    white-space: nowrap;
  }
  .contact__icon {
    flex: none;
    fill: var(--muted);
  }
  .contact__item--web { left: 64px; top: 370px; font-size: 23px; }
  .contact__item--web .contact__icon { margin-right: 12px; }
  .contact__item--phone { left: 115px; top: 438px; font-size: 26px; }
  .contact__item--phone .contact__icon { margin-right: 20px; }
  .contact__item--mail { left: 64px; top: 502px; font-size: 20px; }
  .contact__item--mail .contact__icon { margin-right: 14px; }
</style>
</head>
<body>
<div class="canvas">

  <section class="card card--front">
    <svg class="texture" viewBox="0 0 502 900" role="img" aria-label="Gold and bronze pixel mosaic texture in the top-left and bottom-right corners">
      <defs>
        <linearGradient id="front-top" x1="0" y1="0" x2="1" y2="1">
          <stop offset="0" stop-color="#e0c05a"/>
          <stop offset="0.35" stop-color="#7a6234"/>
          <stop offset="1" stop-color="#3b342c"/>
        </linearGradient>
        <linearGradient id="front-bottom" x1="1" y1="1" x2="0" y2="0">
          <stop offset="0" stop-color="#e6c95e"/>
          <stop offset="0.4" stop-color="#8a6a34"/>
          <stop offset="1" stop-color="#3a332c"/>
        </linearGradient>
      </defs>
      <polygon points="0,0 294,0 185,115 110,195 0,310" fill="url(#front-top)"/>
      <polygon points="502,587 502,900 204,900 320,780 400,690" fill="url(#front-bottom)"/>
    </svg>
    <div class="brand">
      <span class="brand__mark"></span>
      <span class="brand__name">OWEN TASKER</span>
      <span class="brand__tag">STUDIOS</span>
    </div>
  </section>

  <section class="card card--back">
    <svg class="texture" viewBox="0 0 502 900" role="img" aria-label="Muted olive and grey pixel mosaic texture along the lower part of the card">
      <defs>
        <linearGradient id="back-mosaic" x1="0" y1="0" x2="0" y2="1">
          <stop offset="0" stop-color="#5d4e3a"/>
          <stop offset="0.45" stop-color="#6f6a58"/>
          <stop offset="0.75" stop-color="#4e473e"/>
          <stop offset="1" stop-color="#2e2a28"/>
        </linearGradient>
      </defs>
      <rect x="0" y="500" width="502" height="400" fill="url(#back-mosaic)"/>
      <polygon points="0,0 502,0 502,509 257,762 77,582 0,510" fill="var(--card)"/>
    </svg>
    <div class="brand">
      <span class="brand__mark"></span>
      <span class="brand__name">OWEN TASKER</span>
      <span class="brand__tag">STUDIOS</span>
    </div>
    <ul class="contact">
      <li class="contact__item contact__item--web">
        <svg class="contact__icon" width="32" height="32" viewBox="0 0 32 32" aria-hidden="true">
          <circle cx="16" cy="16" r="14" fill="none" stroke="#c9c8c3" stroke-width="2"/>
          <ellipse cx="16" cy="16" rx="6" ry="14" fill="none" stroke="#c9c8c3" stroke-width="2"/>
          <line x1="2" y1="16" x2="30" y2="16" stroke="#c9c8c3" stroke-width="2"/>
          <line x1="5" y1="9" x2="27" y2="9" stroke="#c9c8c3" stroke-width="2"/>
          <line x1="5" y1="23" x2="27" y2="23" stroke="#c9c8c3" stroke-width="2"/>
        </svg>
        <span>taskerlens.examplefolio.net</span>
      </li>
      <li class="contact__item contact__item--phone">
        <svg class="contact__icon" width="28" height="28" viewBox="0 0 24 24" aria-hidden="true">
          <path d="M6.6 10.8c1.4 2.8 3.8 5.1 6.6 6.6l2.2-2.2c.3-.3.7-.4 1-.2 1.1.4 2.3.6 3.6.6.6 0 1 .4 1 1V20c0 .6-.4 1-1 1C10.6 21 3 13.4 3 4c0-.6.4-1 1-1h3.5c.6 0 1 .4 1 1 0 1.3.2 2.5.6 3.6.1.3 0 .7-.2 1z"/>
        </svg>
        <span>323-481-5206</span>
      </li>
      <li class="contact__item contact__item--mail">
        <svg class="contact__icon" width="38" height="26" viewBox="0 0 38 26" aria-hidden="true">
          <path d="M0 0h38v26H0z M3 3v1l16 12L35 4V3z M3 7.5V23h32V7.5L19 19.5z" fill-rule="evenodd"/>
        </svg>
        <span>owentaskerlens@mailbox-example.net</span>
      </li>
    </ul>
  </section>

</div>
</body>
</html>
```